Design a Consultation and HR Services Website "Bright Paths"

Consultation and HR Services
I am looking for a design gives the look and feel of Varden Holt and Quillmere
we need a high-quality graphics website that looks rich and expensive.
we are working as an affiliate for international consultation firms and sole agent for international HR products.
we are a group of consultants for the Middle East.
we will get the global practices to local practices.
Updates

Project Deadline Extended
Reason: I am not getting enough options and designs. I am not getting what I was looking for in matter of look and feel. looking for something rich and luxury with black background and rich font. www.gridmarlow.com www.benitavoss.com 17kendalrow.com/ www.trulo.cc/rd/en/ pemberfold.com/ www.trulo.cc/rd/en/ www.zolmi.com/ www.thegildings.co.uk/ .

Target Market(s)

Corporate all size and industries in GCC

Industry/Entity Type

Management Consulting

Coding

Coded - Design and coding required

Number of Pages Required

5+ page

Font styles to use
Sans Serif
Script

Colors
ffffff
ecf7fb
cee9f5
85cae6
33a6d7
0592cd
000000
848484

Requirements
Must have
• This is the looks and feel that I'm looking for.
• http://www.gridmarlow.com/?channel=display&subchannel=pagemuse
• http://www.benitavoss.com/bvny-private/en/
• http://17kendalrow.com/
• http://www.trulo.cc/rd/en/
• http://pemberfold.com/
• http://www.zolmi.com/
• http://www.thegildings.co.uk/
• Home
• Who we are?
• What we do?
• HR & OD Consultation
• Executive Coaching
• Assesment Cemter
• HRIS & Outsourcing
• Testimonials
• Our Partners
• Contact Us
• We need support on Technical righting...

```html
<!DOCTYPE html>
<html lang="en">
<head>
<meta charset="utf-8">
<title>Bright Paths – Consultation and HR Services</title>
<link href="https://fonts.googleapis.com/css2?family=Great+Vibes&family=Roboto:ital,wght@0,400;0,500;0,700;1,400&display=swap" rel="stylesheet">
<style>
:root{
  --white:#ffffff;
  --ice:#ecf7fb;
  --mist:#cee9f5;
  --sky:#85cae6;
  --azure:#33a6d7;
  --brand:#0592cd;
  --black:#000000;
  --grey:#848484;
  --ink:#333333;
  --script:"Great Vibes", cursive;
  --sans:"Roboto", Arial, sans-serif;
}
*{box-sizing:border-box;margin:0;padding:0}
html,body{width:1200px;height:3390px;overflow:hidden}
body{position:relative;background:var(--white);font-family:var(--sans);color:var(--ink)}
.abs{position:absolute}

/* header */
.site-header{left:0;top:0;width:1200px;height:102px;background:var(--white)}
.menu-toggle{left:74px;top:38px;width:24px;height:18px}
.menu-toggle span{display:block;height:3px;background:var(--grey);margin-bottom:4.5px;border-radius:1px}
.brand{font-family:var(--sans);font-weight:500;color:var(--brand);font-size:24px;display:flex;align-items:center;gap:10px}
.brand .dot{width:14px;height:14px;border-radius:50%;background:var(--brand)}
.site-header .brand{left:0;width:1200px;top:34px;justify-content:center}
.social{right:70px;top:42px;display:flex;gap:14px}
.social i{display:block;width:16px;height:16px;border-radius:50%;background:var(--grey)}
.social i:first-child{background:var(--brand)}

/* hero */
.hero{left:0;top:102px;width:1200px;height:504px;background:linear-gradient(180deg,#4a4644 0%,#6b625c 40%,#3e3a38 100%)}
.hero-title{left:0;width:1200px;top:248px;text-align:center;font-family:var(--script);font-weight:400;font-size:86px;color:var(--white);line-height:1}
.hero-sub{left:330px;width:540px;top:350px;text-align:center;font-size:19px;line-height:30px;color:var(--white)}
.hero-dots{left:0;width:1200px;top:558px;display:flex;justify-content:center;gap:10px}
.hero-dots i{width:10px;height:10px;border-radius:50%;background:var(--white)}
.hero-dots i:first-child{background:var(--azure)}

/* divider */
.divider{left:74px;width:1052px;height:1px;background:var(--mist)}

.section-title{left:0;width:1200px;text-align:center;font-family:var(--script);font-weight:400;font-size:52px;color:var(--black);line-height:1}

/* services */
.service{width:250px;text-align:center}
.service .icon{width:90px;height:90px;margin:0 auto;border-radius:50%;border:2px solid var(--grey);background:linear-gradient(#fafafa,#e2e2e2);display:flex;align-items:center;justify-content:center}
.service.active .icon{border-color:var(--brand);background:var(--white)}
.service h3{margin-top:24px;font-size:21px;font-weight:500;color:var(--black)}
.service.active h3{color:var(--brand)}
.service p{margin-top:10px;font-size:13px;line-height:22px;color:var(--ink)}

/* feature blocks */
.photo{width:600px;height:404px}
.panel{width:600px;height:404px;background:var(--brand);color:var(--white);padding:56px 68px 0 67px}
.panel h2{font-family:var(--script);font-weight:400;font-size:50px;line-height:1}
.panel p{margin-top:28px;font-size:13.5px;line-height:23px;width:460px}
.btn{display:inline-block;margin-top:36px;width:190px;height:46px;line-height:44px;text-align:center;font-size:14px;color:var(--white);border:2px solid var(--black)}
.btn.solid{background:var(--black)}

/* testimonials */
.quote{left:110px;width:980px;top:2560px;text-align:center;font-style:italic;font-size:13.5px;line-height:25px;color:var(--ink)}
.arrow{top:2628px}
.avatar{left:560px;top:2660px;width:80px;height:80px;border-radius:50%;border:3px solid var(--mist);background:linear-gradient(#d9d9d9,#9a9a9a)}
.quote-mark{left:570px;top:2712px;width:60px;text-align:center;font-family:Georgia,serif;font-size:48px;font-weight:700;color:var(--brand);line-height:1}

/* footer */
.contact{left:0;top:2814px;width:1200px;height:434px;background:var(--black);color:var(--white)}
.contact h2{position:absolute;top:50px;font-family:var(--script);font-weight:400;font-size:50px;line-height:1}
.field{position:absolute;border:1px solid var(--white);font-size:13px;padding:12px 10px;color:var(--white)}
.send{position:absolute;left:515px;top:355px;width:190px;height:45px;line-height:45px;text-align:center;background:var(--azure);color:var(--white);font-size:15px}
.info{position:absolute;left:766px;top:138px;font-size:13px;line-height:20px;color:var(--grey)}
.info .name{color:var(--azure);font-weight:700;font-size:16px;margin-bottom:8px}
.info ul{list-style:none;margin-top:14px}
.info li{display:flex;align-items:center;gap:14px;height:29px;color:var(--white)}
.info li:first-child{color:var(--azure)}
.info svg{flex:none}

.site-footer .brand{left:0;width:1200px;top:3270px;justify-content:center}
.copyright{left:0;width:1200px;top:3340px;text-align:center;font-size:12px;color:var(--grey)}
</style>
</head>
<body>

<header class="site-header abs">
  <div class="menu-toggle abs"><span></span><span></span><span></span></div>
  <div class="brand abs"><span class="dot"></span>Bright Paths</div>
  <div class="social abs"><i></i><i></i><i></i><i></i></div>
</header>

<section class="hero abs" role="img" aria-label="Team of business professionals in suits standing in an office"></section>
<h1 class="hero-title abs">Bright Paths</h1>
<p class="hero-sub abs">Duis aliquam nibh a dui iaculis viverra id a velit egestas risus in magna varius commodo.</p>
<svg class="abs" style="left:86px;top:320px" width="20" height="60" viewBox="0 0 20 60"><path d="M18 2 2 30l16 28" fill="none" stroke="rgba(255,255,255,.5)" stroke-width="2"/></svg>
<svg class="abs" style="left:1094px;top:320px" width="20" height="60" viewBox="0 0 20 60"><path d="M2 2l16 28L2 58" fill="none" stroke="rgba(255,255,255,.5)" stroke-width="2"/></svg>
<div class="hero-dots abs"><i></i><i></i><i></i><i></i></div>

<div class="divider abs" style="top:674px"></div>
<h2 class="section-title abs" style="top:718px">What We Do?</h2>

<div class="service active abs" style="left:69px;top:825px">
  <div class="icon"><svg width="40" height="40" viewBox="0 0 40 40" fill="var(--black)"><circle cx="14" cy="10" r="5"/><path d="M8 34l3-18h6l3 18z"/><circle cx="27" cy="14" r="4"/><path d="M22 34l2-14h6l2 14z"/></svg></div>
  <h3>Strategy</h3>
  <p>Sed vel magna vel eros adipiscing adipiscing eu sit amet turpis. Mauris et massa sed lacus tempus pellentesque.</p>
</div>
<div class="service abs" style="left:338px;top:825px">
  <div class="icon"><svg width="40" height="40" viewBox="0 0 40 40" fill="#555"><circle cx="20" cy="10" r="5"/><path d="M14 34V18h12v16z"/><circle cx="9" cy="13" r="4"/><path d="M4 32V20h9v12z"/><circle cx="31" cy="13" r="4"/><path d="M27 32V20h9v12z"/></svg></div>
  <h3>People</h3>
  <p>Sed vel magna vel eros adipiscing adipiscing eu sit amet turpis. Mauris et massa sed lacus tempus pellentesque.</p>
</div>
<div class="service abs" style="left:609px;top:825px">
  <div class="icon"><svg width="40" height="40" viewBox="0 0 40 40" fill="none" stroke="#555" stroke-width="4"><path d="M8 18a12 12 0 0 1 22-6"/><path d="M32 22a12 12 0 0 1-22 6"/><path d="M31 4v9h-9M9 36v-9h9" stroke-width="3"/></svg></div>
  <h3>Process</h3>
  <p>Sed vel magna vel eros adipiscing adipiscing eu sit amet turpis. Mauris et massa sed lacus tempus pellentesque.</p>
</div>
<div class="service abs" style="left:881px;top:825px">
  <div class="icon"><svg width="40" height="40" viewBox="0 0 40 40" fill="none" stroke="#555" stroke-width="4" stroke-dasharray="4 3"><circle cx="15" cy="24" r="8"/><circle cx="29" cy="12" r="6"/></svg></div>
  <h3>Technology</h3>
  <p>Sed vel magna vel eros adipiscing adipiscing eu sit amet turpis. Mauris et massa sed lacus tempus pellentesque.</p>
</div>

<div class="photo abs" style="left:0;top:1141px;background:linear-gradient(180deg,#e8e8e8,#8d8d8d 60%,#3c3c3c)" role="img" aria-label="Group of business people in dark suits walking forward"></div>
<div class="panel abs" style="left:600px;top:1141px">
  <h2>Who We Are?</h2>
  <p>Nunc consequat congue nulla eu imperdiet. Donec in est erat, id malesuada turpis. Nunc a dui id turpis convallis semper. Nunc dignissim lectus vitae eros placerat euismod. Aenean lacinia sodales eros, sit amet molestie enim consectetur eget. Sed vel magna vel eros adipiscing adipiscing eu sit amet turpis.</p>
  <span class="btn solid">Learn More</span>
</div>

<div class="panel abs" style="left:0;top:1545px">
  <h2>Who We Serve?</h2>
  <p>Nunc consequat congue nulla eu imperdiet. Donec in est erat, id malesuada turpis. Nunc a dui id turpis convallis semper. Nunc dignissim lectus vitae eros placerat euismod. Aenean lacinia sodales eros, sit amet molestie enim consectetur eget. Sed vel magna vel eros adipiscing adipiscing eu sit amet turpis.</p>
  <span class="btn">Learn More</span>
</div>
<div class="photo abs" style="left:600px;top:1545px;background:linear-gradient(135deg,#f2f2f2,#b9c2cc 50%,#2b3442)" role="img" aria-label="Business colleagues shaking hands over a laptop in a meeting"></div>

<div class="photo abs" style="left:0;top:1949px;background:linear-gradient(135deg,#e9ecef,#a7aeb5 50%,#262626)" role="img" aria-label="Smiling customer service agent wearing a headset at a desk"></div>
<div class="panel abs" style="left:600px;top:1949px">
  <h2>Whom We Help?</h2>
  <p>Nunc consequat congue nulla eu imperdiet. Donec in est erat, id malesuada turpis. Nunc a dui id turpis convallis semper. Nunc dignissim lectus vitae eros placerat euismod. Aenean lacinia sodales eros, sit amet molestie enim consectetur eget. Sed vel magna vel eros adipiscing adipiscing eu sit amet turpis.</p>
  <span class="btn">Learn More</span>
</div>

<div class="divider abs" style="top:2418px"></div>
<h2 class="section-title abs" style="top:2462px">Testimonials</h2>
<p class="quote abs">Vestibulum vel metus sit amet turpis bibendum tincidunt vel sit amet quam. Pellentesque habitant morbi tristique senectus et netus et malesuada fames ac turpis egestas. Nunc consequat congue nulla eu imperdiet. Donec in est erat, id malesuada turpis. Nunc a dui id turpis convallis semper. Nunc dignissim lectus vitae eros placerat euismod. Aenean lacinia sodales eros, sit amet molestie enim consectetur eget.</p>
<svg class="arrow abs" style="left:74px" width="18" height="28" viewBox="0 0 18 28"><path d="M16 2 4 14l12 12" fill="none" stroke="#bbb" stroke-width="4"/></svg>
<svg class="arrow abs" style="left:1106px" width="18" height="28" viewBox="0 0 18 28"><path d="M2 2l12 12L2 26" fill="none" stroke="#bbb" stroke-width="4"/></svg>
<div class="avatar abs" role="img" aria-label="Portrait of the client giving the testimonial"></div>
<div class="quote-mark abs">&ldquo;&rdquo;</div>

<footer class="contact abs">
  <h2 style="left:77px">Let Us Talk</h2>
  <h2 style="left:766px">Contact Address</h2>
  <div class="field" style="left:77px;top:131px;width:307px;height:44px">Name</div>
  <div class="field" style="left:396px;top:131px;width:309px;height:44px">Email Address</div>
  <div class="field" style="left:77px;top:185px;width:628px;height:152px">Message</div>
  <div class="send">Send Message</div>
  <div class="info">
    <div class="name">Bright Paths</div>
    <div>2210 Harbor Lane,</div>
    <div>Lakemont CA 95014</div>
    <ul>
      <li><svg width="14" height="14" viewBox="0 0 14 14"><path d="M3 1l3 3-2 2a8 8 0 0 0 4 4l2-2 3 3-2 2C6 13 1 8 1 3z" fill="currentColor"/></svg>(555) 014-2280</li>
      <li><svg width="14" height="14" viewBox="0 0 14 14" fill="currentColor"><rect x="1" y="5" width="12" height="8"/><rect x="3" y="1" width="8" height="4"/></svg>(555) 014-2280</li>
      <li><svg width="14" height="14" viewBox="0 0 14 14" fill="currentColor"><rect x="3" y="0" width="8" height="14" rx="1"/></svg>(555) 014-2280</li>
      <li><svg width="14" height="14" viewBox="0 0 14 14"><path d="M3 1l3 3-2 2a8 8 0 0 0 4 4l2-2 3 3-2 2C6 13 1 8 1 3z" fill="currentColor"/></svg>info@brightpaths.com</li>
    </ul>
  </div>
</footer>

<div class="site-footer">
  <div class="brand abs"><span class="dot"></span>Bright Paths</div>
  <p class="copyright abs">Copyright © 2015. All Right Reserved. Privacy Policy</p>
</div>

</body>
</html>
```